Website Design for my CNC machine Shop.

I need a new website for my Machining Company.

It can be a simple website that acts more like an "Online Business card" I has to highlight the services I provide and give Companies the confidence to engage my services.

I needs it to be a really modern or even a little futuristic promoting my Company.

I have just moved locations and have renovated the premises and would be great to let everyone know along with a new website.

If you can help with linking it to search engines to help get more exposure that would be great.

It needs to accommodate the three main services I provide which will include capacities of each machine (within that service) and maybe a couple images.
CNC Machining (5-axis, 3-axis)
EDM Wire cutting
3D Metal Printing
Along with home page and Contact page

I have two websites and you can use the txt from either/combination of these.
www.korvanmetalworks.com.au
(no longer do Laser Marking and etching but now do 3D metal Printing)
www.brislotech.com.au

Happy to chat further with the designer

Company logo's provided.

For Images: I am happy to use Pixelgrove and can purchase any images you like
EDM Wire cut
https://www.pixelgrove.com/search/edm-wire-cutting

CNC Machining:
https://www.pixelgrove.com/search/vertical-cnc-machining
Don't use any with engines or motor vehicle parts

3D metal Printing
https://www.pixelgrove.com/search/slm-metal-printing

Target Market(s)

Defence, Aerospace, Medical, HIgh Precision

Industry/Entity Type

Mechanical Engineering

Coding

Coded - Design and coding required

Number of Pages Required

5+ page

Requirements
Must have
• Home page, 3 services, Contacts. Can add image to each of the services

```html
<!DOCTYPE html>
<html lang="en">
<head>
<meta charset="utf-8">
<title>Tarlow Precision Engineering</title>
<link href="https://fonts.googleapis.com/css2?family=Poppins:wght@400;500;600;700&display=swap" rel="stylesheet">
<style>
:root{
  --green:#36a878;
  --green-dark:#2b8b62;
  --ink:#1d2326;
  --dark:#1b2124;
  --grey:#eceded;
  --text:#5b6266;
  --white:#ffffff;
}
*{box-sizing:border-box;margin:0;padding:0}
html,body{width:1200px;height:5336px;overflow:hidden}
body{font-family:"Poppins",sans-serif;color:var(--ink);background:var(--white);position:relative}
.abs{position:absolute}
.btn{display:inline-block;background:var(--green);color:#fff;font-weight:600;font-size:17px;text-transform:uppercase;padding:18px 34px;clip-path:polygon(0 0,100% 0,100% 70%,92% 100%,0 100%)}
.label{color:var(--green);font-size:16px;font-weight:600;text-transform:uppercase;letter-spacing:1px}
.title{font-size:40px;font-weight:600;color:var(--ink);line-height:1.25}
.center{text-align:center;width:100%}

/* hero */
.hero{top:0;left:0;width:1200px;height:652px;background:linear-gradient(120deg,#0a1c1e 0%,#18433f 45%,#0d2527 100%)}
.hero-glow{top:0;left:0;width:1200px;height:652px;background:radial-gradient(circle at 68% 40%,rgba(240,190,110,.5) 0,rgba(80,140,120,.22) 22%,rgba(10,30,32,0) 50%)}
.topbar{top:8px;left:100px;right:100px;height:28px;color:#fff;font-size:16px;display:flex;justify-content:space-between;align-items:center}
.topbar span{display:flex;align-items:center;gap:10px}
.dot-ic{width:22px;height:22px;border-radius:50%;background:var(--green);display:inline-block}
.nav{top:48px;left:160px;width:888px;height:68px;background:#fff;border-radius:6px;display:flex;align-items:center;justify-content:space-between;padding:0 40px;font-size:17px;font-weight:500}
.nav .group{display:flex;gap:56px}
.nav .active{border-bottom:3px solid var(--green);padding-bottom:4px}
.brand{font-size:38px;font-weight:700;color:var(--ink);letter-spacing:2px}
.hero-pre{top:220px;left:100px;color:#fff;font-size:24px}
.hero-h{top:252px;left:100px;color:#fff;font-size:56px;font-weight:600;line-height:1.08}
.hero-btn{top:476px;left:100px}
.dots{top:612px;left:540px;display:flex;gap:8px}
.dots i{width:22px;height:8px;border-radius:4px;background:rgba(255,255,255,.5);display:block}
.dots i:first-child{background:#fff;width:30px}
.follow{top:240px;left:1070px;color:#fff;font-size:14px;writing-mode:vertical-rl;letter-spacing:2px}
.follow-ic{left:1072px;width:20px;height:20px;border-radius:50%;border:2px solid #fff}

/* about */
.about-img{top:720px;left:124px;width:440px;height:370px;background:linear-gradient(135deg,#2f4850,#8aa3ad 50%,#3b5058)}
.about-accent{top:1040px;left:156px;width:70px;height:70px;background:var(--green);display:flex;align-items:center;justify-content:center}
.about-txt{top:736px;left:612px;width:480px}
.about-txt h2{font-size:34px}
.about-txt p{font-size:16px;color:var(--text);line-height:1.7;margin:16px 0 28px}

/* services */
.services{top:1200px;left:0;width:1200px;height:880px;background:var(--grey)}
.card{top:1428px;width:312px;height:480px;background:#fff;box-shadow:0 6px 20px rgba(0,0,0,.06)}
.card .ph{height:300px}
.card h3{font-size:20px;font-weight:600;margin:22px 18px 8px}
.card p{font-size:15px;color:var(--text);line-height:1.6;margin:0 18px}
.card.feature{background:var(--green)}
.card.feature h3,.card.feature p{color:#fff}

/* industries */
.gear{top:2512px;left:380px;width:440px;height:480px;border-radius:50%;background:radial-gradient(circle,#eceeef 0,#dfe2e3 70%,#eef0f1 100%);display:flex;align-items:center;justify-content:center}
.gear span{background:#fff;padding:10px 30px;font-size:40px;font-weight:700;color:var(--ink);letter-spacing:2px}
.node{width:56px;height:56px;border-radius:50%;display:flex;align-items:center;justify-content:center;transform:translate(-28px,-28px);color:var(--green)}
.node.light{background:#fff;border:4px solid var(--green)}
.node.darkn{background:#fff;border:4px solid var(--dark)}
.ind{font-size:16px;font-weight:600;color:var(--ink);white-space:nowrap}

/* why */
.why{top:3220px;left:0;width:1200px;height:500px;background:var(--dark)}
.why-img{top:3220px;left:620px;width:580px;height:500px;background:linear-gradient(100deg,#1b2124 0%,#5c4a3a 45%,#c98a48 65%,#3a3430 100%)}
.why h2{position:absolute;top:80px;left:100px;color:#fff;font-size:38px;font-weight:600}
.feat{display:flex;align-items:center;gap:16px;color:#fff;font-size:16px;line-height:1.4}
.feat .ic{width:52px;height:52px;border-radius:50%;background:var(--green);flex:none}

/* contact */
.contact{top:3660px;left:200px;width:820px;height:460px;background:#fff;box-shadow:0 10px 30px rgba(0,0,0,.12);padding:40px 28px}
.contact h2{font-size:34px;font-weight:600}
.contact p{font-size:16px;color:var(--text);line-height:1.5;width:420px;margin:10px 0 30px}
.call{top:3620px;left:680px;width:340px;height:170px;background:var(--green);color:#fff;padding:26px;font-size:16px;line-height:1.5}
.field{position:absolute;border:1px solid #d6d8d9;font-size:15px;color:var(--text);padding:12px}

/* gallery */
.g{top:4368px;height:320px}
.gcap{display:flex;align-items:center;justify-content:center;color:#fff;font-size:24px;font-weight:600}

/* footer */
.footer{top:4780px;left:0;width:1200px;height:556px;background:var(--dark);color:#cfd3d5}
.fcol h4{color:#fff;font-size:18px;font-weight:600;margin-bottom:20px}
.fcol p,.fcol li{font-size:16px;line-height:1.9;list-style:none}
.news{top:4860px;left:908px;width:290px;height:290px;background:#272e32;padding:26px}
.bottom{top:5272px;left:0;width:1200px;height:64px;background:#14191b;color:#cfd3d5;font-size:15px;display:flex;align-items:center;justify-content:space-between;padding:0 100px}
.soc{width:26px;height:26px;border-radius:50%;background:#fff;display:inline-block;margin-left:8px}
</style>
</head>
<body>

<section class="abs hero" role="img" aria-label="Close-up photo of an EDM wire cutting machine sparking on metal"></section>
<div class="abs hero-glow"></div>
<div class="abs topbar">
  <span><i class="dot-ic"></i>Mail Us : info@tarlowengineering.com.au</span>
  <span><i class="dot-ic"></i>Call Us : +61 400 555 210</span>
</div>
<nav class="abs nav">
  <div class="group"><span class="active">HOME</span><span>ABOUT</span></div>
  <span class="brand">TARLOW</span>
  <div class="group"><span>SERVICES</span><span>CONTACT</span></div>
</nav>
<p class="abs hero-pre">We Offer A</p>
<h1 class="abs hero-h">Comprehensive<br>And Professional<br>Service</h1>
<a class="abs btn hero-btn">Get In Touch Now</a>
<div class="abs dots"><i></i><i></i><i></i><i></i></div>
<span class="abs follow">FOLLOW US</span>
<span class="abs follow-ic" style="top:380px"></span>
<span class="abs follow-ic" style="top:412px"></span>
<span class="abs follow-ic" style="top:444px"></span>

<div class="abs about-img" role="img" aria-label="Photo of CNC milling tool cutting a metal part"></div>
<div class="abs about-accent"><svg width="40" height="40" viewBox="0 0 40 40"><circle cx="20" cy="20" r="17" fill="none" stroke="#fff" stroke-width="3"/><path d="M16 13 L28 20 L16 27Z" fill="#fff"/></svg></div>
<div class="abs about-txt">
  <p class="label" style="margin:0">We Are An Innovative Company</p>
  <h2 class="title" style="margin-top:10px">That Specialise In Technical And Creative Engineering</h2>
  <p>Our core sectors of expertise are in EDM wire cutting, 3D Metal Printing and CNC machining. With our combination of highly skilled staff and sophisticated machinery we offer a comprehensive and professional service.</p>
  <a class="btn">Read More</a>
</div>

<section class="abs services"></section>
<p class="abs label center" style="top:1280px">Machine Services</p>
<h2 class="abs title center" style="top:1312px">Comprehensive And Professional Service</h2>
<div class="abs card" style="left:100px">
  <div class="ph" role="img" aria-label="Photo of a vertical CNC machining centre" style="background:linear-gradient(160deg,#f2f2f2,#c9ced1)"></div>
  <h3>CNC Machining</h3>
  <p>With our combination of high quality Vextra Machining Centres</p>
</div>
<div class="abs card feature" style="left:444px">
  <div class="ph" role="img" aria-label="Photo of an EDM wire cutting machine" style="background:linear-gradient(160deg,#4a4d4f,#a7acae 55%,#2e3133)"></div>
  <h3>EDM Wire Cutting</h3>
  <p>We operate Swiss manufactured Altmont EDM Machines which</p>
</div>
<div class="abs card" style="left:788px">
  <div class="ph" role="img" aria-label="Photo of a 3D metal printer" style="background:linear-gradient(160deg,#ffffff,#d7d9da)"></div>
  <h3>3D Metal Printing</h3>
  <p>Stemming from an engineering background and we well</p>
</div>
<a class="abs btn" style="top:1948px;left:508px">View Project</a>

<p class="abs label center" style="top:2196px">High Quality Services</p>
<h2 class="abs title center" style="top:2236px">We Offer A Range Of High Quality<br>Services To A Variety Of Industries</h2>
<div class="abs gear" role="img" aria-label="Large grey gear illustration behind the company name"><span>TARLOW</span></div>
<svg width="0" height="0" style="position:absolute"><defs><symbol id="tick" viewBox="0 0 24 24"><path d="M5 12.5 L10 17 L19 7" fill="none" stroke="currentColor" stroke-width="3" stroke-linecap="round" stroke-linejoin="round"/></symbol></defs></svg>
<div class="abs node light" style="left:600px;top:2480px"><svg width="26" height="26"><use href="#tick"/></svg></div>
<div class="abs node darkn" style="left:736px;top:2516px"><svg width="26" height="26"><use href="#tick"/></svg></div>
<div class="abs node light" style="left:836px;top:2616px"><svg width="26" height="26"><use href="#tick"/></svg></div>
<div class="abs node darkn" style="left:872px;top:2752px"><svg width="26" height="26"><use href="#tick"/></svg></div>
<div class="abs node light" style="left:836px;top:2888px"><svg width="26" height="26"><use href="#tick"/></svg></div>
<div class="abs node darkn" style="left:736px;top:2988px"><svg width="26" height="26"><use href="#tick"/></svg></div>
<div class="abs node light" style="left:600px;top:3024px"><svg width="26" height="26"><use href="#tick"/></svg></div>
<div class="abs node darkn" style="left:464px;top:2988px"><svg width="26" height="26"><use href="#tick"/></svg></div>
<div class="abs node light" style="left:364px;top:2888px"><svg width="26" height="26"><use href="#tick"/></svg></div>
<div class="abs node darkn" style="left:328px;top:2752px"><svg width="26" height="26"><use href="#tick"/></svg></div>
<div class="abs node light" style="left:364px;top:2616px"><svg width="26" height="26"><use href="#tick"/></svg></div>
<div class="abs node darkn" style="left:464px;top:2516px"><svg width="26" height="26"><use href="#tick"/></svg></div>
<span class="abs ind" style="left:540px;top:2400px">Prototyping</span>
<span class="abs ind" style="left:780px;top:2508px">Gauges</span>
<span class="abs ind" style="left:880px;top:2608px">Jigs &amp; Fixtures</span>
<span class="abs ind" style="left:920px;top:2744px">Press Tools</span>
<span class="abs ind" style="left:880px;top:2880px">Assemblies</span>
<span class="abs ind" style="left:780px;top:2998px">Automated Systems</span>
<span class="abs ind" style="left:562px;top:3068px">Tooling</span>
<span class="abs ind" style="left:322px;top:2998px">Nozzles</span>
<span class="abs ind" style="left:200px;top:2864px;text-align:center">Custom<br>Machining</span>
<span class="abs ind" style="left:122px;top:2744px">Work Stations</span>
<span class="abs ind" style="left:168px;top:2626px">Production</span>
<span class="abs ind" style="left:216px;top:2508px">Keyway Cutting</span>

<section class="abs why"><h2>Why Choose Us</h2>
  <div class="abs feat" style="top:160px;left:100px;width:300px"><i class="ic"></i>Capability of producing components</div>
  <div class="abs feat" style="top:160px;left:420px;width:200px"><i class="ic"></i>Extensive range of machinery</div>
  <div class="abs feat" style="top:244px;left:100px;width:300px"><i class="ic"></i>Latest technology of wire cutting</div>
  <div class="abs feat" style="top:244px;left:420px;width:200px"><i class="ic"></i>Highly skilled staff</div>
</section>
<div class="abs why-img" role="img" aria-label="Photo of a machinist grinding metal with sparks"></div>

<section class="abs contact">
  <h2>Send Us A Message</h2>
  <p>Please include your contact details and a short message and we will get back to you as soon as we can.</p>
  <div class="field" style="top:200px;left:28px;width:230px;height:52px">First Name</div>
  <div class="field" style="top:200px;left:272px;width:230px;height:52px">Last Name</div>
  <div class="field" style="top:200px;left:516px;width:244px;height:116px">Message</div>
  <div class="field" style="top:264px;left:28px;width:230px;height:52px">Email</div>
  <div class="field" style="top:264px;left:272px;width:230px;height:52px">Phone</div>
  <a class="btn" style="position:absolute;top:340px;left:28px;font-size:16px;padding:14px 24px">Submit Now</a>
</section>
<div class="abs call">We will get back to you, or call us everyday, 09.00am - 12.00pm<br><br><b>+61 400 555 210</b></div>

<p class="abs label center" style="top:4236px">Features Gallery</p>
<h2 class="abs title center" style="top:4276px">View Industrial Projects</h2>
<div class="abs g" style="left:0;width:156px;background:linear-gradient(160deg,#3a3f42,#9aa0a3)" role="img" aria-label="Photo of a machined steel part"></div>
<div class="abs g" style="left:184px;width:268px;background:linear-gradient(160deg,#eef0f1,#9aa1a5)" role="img" aria-label="Photo of a milled aluminium bracket"></div>
<div class="abs g gcap" style="left:470px;width:264px;background:linear-gradient(160deg,#4bbb8a,#2b8b62)" role="img" aria-label="Project 1 photo with green overlay">PROJECT 1</div>
<div class="abs g" style="left:752px;width:264px;background:linear-gradient(160deg,#2a2d2f,#b8bdc0)" role="img" aria-label="Photo of a precision turned pin"></div>
<div class="abs g" style="left:1044px;width:156px;background:linear-gradient(160deg,#c4c7c8,#6f7477)" role="img" aria-label="Photo of machined metal discs"></div>

<footer class="abs footer">
  <div class="abs fcol" style="top:80px;left:100px;width:230px">
    <div style="font-size:40px;font-weight:700;color:#fff;letter-spacing:2px;margin-bottom:40px">TARLOW</div>
    <p>Being a high precision engineering company we offer a range of high quality services.</p>
  </div>
  <div class="abs fcol" style="top:120px;left:368px;width:220px">
    <h4>QUICK CONTACT</h4>
    <p>Unit 4, 12 Keller Road,<br>DANDENONG</p>
    <p style="color:var(--green);margin-top:20px">03 9000 4127</p>
  </div>
  <div class="abs fcol" style="top:120px;left:612px">
    <h4>QUICK LINK</h4>
    <ul><li>Home</li><li>EDM Wire cutting</li><li>CNC Machining</li><li>3D Metal Printing</li><li>Contact</li></ul>
  </div>
  <div class="abs" style="top:410px;left:380px;font-size:16px;color:#fff;display:flex;gap:60px">
    <span><i class="dot-ic" style="vertical-align:middle;width:18px;height:18px;margin-right:8px"></i>info@tarlowengineering.com.au</span>
    <span><i class="dot-ic" style="vertical-align:middle;width:18px;height:18px;margin-right:8px"></i>+61 400 555 210</span>
  </div>
</footer>
<div class="abs news">
  <h4 style="color:#fff;font-size:18px;font-weight:600">STAY IN TOUCH</h4>
  <p style="font-size:15px;line-height:1.6;margin:16px 0 40px;color:#cfd3d5">Subscribe to our newsletter so we can keep you updated with offers and discounts</p>
  <div style="display:flex;height:56px"><div style="flex:1;background:#1b2124;color:#cfd3d5;padding:16px;font-size:15px">Email</div><div style="width:60px;background:var(--green);display:flex;align-items:center;justify-content:center"><svg width="22" height="22" viewBox="0 0 22 22"><path d="M3 11 H18 M12 5 L18 11 L12 17" stroke="#fff" stroke-width="2.5" fill="none"/></svg></div></div>
</div>
<div class="abs bottom"><span>© 2024 by TARLOW . All right reserved.</span><span><i class="soc"></i><i class="soc"></i><i class="soc"></i><i class="soc"></i></span></div>

</body>
</html>
```